The Wellness Barn Business Card

Info for the front..... (in whichever order and layout looks best)
Carla Penhallow
Physiotherapist
4/37 Upper Creekbank Rd
Tallowbrook
QLD 4712
0462305178
carlapenhallow57@mailbox.example
www.thewellnessbarn.example.au
on the back I would like to be able to write appointments so probably just that heading with lines.
I like a sort of rustic style but mostly professional, colours in naturals, beige, brown, green etc. I dont mind if the logo colour is changed slightly to suit.

```html
<!DOCTYPE html>
<html lang="en">
<head>
<meta charset="utf-8">
<title>The Wellness Barn – Business Card</title>
<link href="https://fonts.googleapis.com/css2?family=Kumbh+Sans:wght@400;700&display=swap" rel="stylesheet">
<style>
  :root {
    --backdrop: #b6b59f;
    --card: #ffffff;
    --forest: #2a411d;
    --ink: #0d0d0d;
    --leaf-soft: rgba(150, 200, 120, 0.28);
    --leaf-faint: rgba(150, 200, 120, 0.0);
    --rule: #6a6a6a;
  }
  * { margin: 0; padding: 0; box-sizing: border-box; }
  html, body {
    width: 764px; height: 1200px; overflow: hidden;
    background: var(--backdrop);
    font-family: "Kumbh Sans", sans-serif;
    color: var(--ink);
  }
  .stage { position: relative; width: 764px; height: 1200px; }
  .card {
    position: absolute; left: 132px; width: 500px; height: 324px;
    background: var(--card); overflow: hidden;
  }
  .card--front { top: 242px; }
  .card--back { top: 634px; }

  .wave-texture { position: absolute; }
  .card--front .wave-texture {
    left: 0; right: 0; bottom: 0; height: 200px;
    background:
      radial-gradient(ellipse 70% 60% at 20% 90%, var(--leaf-soft), var(--leaf-faint) 70%),
      radial-gradient(ellipse 60% 50% at 70% 95%, var(--leaf-soft), var(--leaf-faint) 70%);
  }
  .card--back .wave-texture {
    left: 0; right: 0; bottom: 0; height: 220px;
    background:
      radial-gradient(ellipse 60% 60% at 80% 70%, var(--leaf-soft), var(--leaf-faint) 70%),
      radial-gradient(ellipse 70% 50% at 40% 100%, var(--leaf-soft), var(--leaf-faint) 70%);
  }

  .accent-bar { position: absolute; top: 0; width: 25px; height: 69px; background: var(--forest); }
  .card--front .accent-bar { left: 31px; }
  .card--back .accent-bar { left: 446px; }

  .tile { position: absolute; width: 18px; height: 18px; border-radius: 4px; }
  .tile--dark { background: var(--ink); }
  .tile--green { background: var(--forest); }

  .brand-name { position: absolute; color: var(--forest); font-weight: 700; white-space: nowrap; }
  .card--front .brand-name { right: 22px; top: 36px; font-size: 11px; }
  .card--back .brand-name { left: 0; right: 0; top: 50px; text-align: center; font-size: 26px; }

  .identity { position: absolute; left: 23px; top: 66px; width: 440px; text-align: center; }
  .identity__name {
    font-size: 42px; font-weight: 700; letter-spacing: -0.5px; line-height: 1;
    white-space: nowrap;
  }
  .identity__role { font-size: 21px; font-weight: 400; line-height: 1; margin-top: 5px; white-space: nowrap; }

  .contact-list { position: absolute; left: 78px; top: 161px; list-style: none; }
  .contact-list li {
    display: flex; align-items: center; height: 18px; margin-bottom: 14px;
    font-size: 13.5px; white-space: nowrap;
  }
  .contact-list li:nth-child(2) { margin-bottom: 15px; }
  .contact-icon { width: 18px; height: 18px; margin-right: 10px; flex: none; }

  .write-lines { position: absolute; left: 60px; width: 381px; top: 139px; }
  .write-lines span {
    display: block; height: 0; border-top: 1px dotted var(--rule); margin-bottom: 22px;
  }
</style>
</head>
<body>
<div class="stage">

  <section class="card card--front">
    <div class="wave-texture" role="img" aria-label="Soft green flowing wave line texture"></div>
    <div class="accent-bar"></div>
    <div class="brand-name">The Wellness Barn</div>

    <div class="identity">
      <h1 class="identity__name">Carla Penhallow</h1>
      <p class="identity__role">Physiotherapist</p>
    </div>

    <ul class="contact-list">
      <li>
        <svg class="contact-icon" viewBox="0 0 18 18"><circle cx="9" cy="9" r="9" fill="#0d0d0d"/><path d="M9 3.8a3.4 3.4 0 0 0-3.4 3.4c0 2.5 3.4 6.2 3.4 6.2s3.4-3.7 3.4-6.2A3.4 3.4 0 0 0 9 3.8z" fill="#fff"/><circle cx="9" cy="7.2" r="1.3" fill="#0d0d0d"/></svg>
        4/37 Upper Creekbank Rd, Tallowbrook, QLD 4712.
      </li>
      <li>
        <svg class="contact-icon" viewBox="0 0 18 18"><circle cx="9" cy="9" r="9" fill="#0d0d0d"/><path d="M6.2 4.6l1.5-.3 1 2.2-1 .9a6 6 0 0 0 2.9 2.9l.9-1 2.2 1-.3 1.5c-.2.6-.8.9-1.4.8A8 8 0 0 1 5.4 6c-.1-.6.2-1.2.8-1.4z" fill="#fff"/></svg>
        0462305178
      </li>
      <li>
        <svg class="contact-icon" viewBox="0 0 18 18"><circle cx="9" cy="9" r="9" fill="#0d0d0d"/><rect x="4.5" y="6" width="9" height="6.2" fill="none" stroke="#fff" stroke-width="0.9"/><path d="M4.5 6l4.5 3.6L13.5 6M4.5 12.2l3.3-3M13.5 12.2l-3.3-3" fill="none" stroke="#fff" stroke-width="0.9"/></svg>
        carlapenhallow57@mailbox.example
      </li>
      <li>
        <svg class="contact-icon" viewBox="0 0 18 18"><circle cx="9" cy="9" r="9" fill="#0d0d0d"/><g fill="none" stroke="#fff" stroke-width="0.8"><circle cx="9" cy="9" r="4.5"/><ellipse cx="9" cy="9" rx="2" ry="4.5"/><path d="M4.5 9h9M5.2 6.7h7.6M5.2 11.3h7.6"/></g></svg>
        www.thewellnessbarn.example.au
      </li>
    </ul>

    <div class="tile tile--dark" style="left:472px; top:272px;"></div>
    <div class="tile tile--green" style="left:453px; top:295px;"></div>
  </section>

  <section class="card card--back">
    <div class="wave-texture" role="img" aria-label="Soft green flowing wave line texture"></div>
    <div class="accent-bar"></div>
    <div class="brand-name">The Wellness Barn</div>

    <div class="write-lines">
      <span></span><span></span><span></span><span></span><span></span><span></span><span></span>
    </div>

    <div class="tile tile--dark" style="left:12px; top:274px;"></div>
    <div class="tile tile--green" style="left:31px; top:296px;"></div>
  </section>

</div>
</body>
</html>
```